Web design for our new company

We need a web design for our product and for our company.
And the main is our Product tool called "veltor".
----------------------------------------------------------
[Our company's Goal]
Make organization’s communication smooth and healthy with transparency and efficiency for works and tasks in all levels with our workflow tool.

[Our Mission]
Our mission is to achieve business goals with customers.
We work together to identify the goals for your company, guides your strategy and bring the technology answers which best fit to achieve the goals.

[What we do]
We have a workflow tool "veltor"
- Very simple end-user configurable workflow for any company processes
(Targeting small-med size company)
- Graphical & fun features for startup users
- Simple and easy task control with outlook e-mail look & feel
- Non charged skill up guidance
- Additional features with;
Multiple delegation
Clear status for each owner
Task owner management console with due date reminders&reporting

Others
1. System Development & Implementation Service
Our client list includes a wide variety of small to medium to major sized enterprises.
We can offer from full-scratch based development to packaged system implementation.

2. Project Management(PM) Service
We will provide end-to-end PM service with experienced PM.
Our service is not only “managing” but “leading” to bring success to achieve the goal.

3.Consultation Service

Consulting services to a wide range of fields such as creating business strategy, business process Kaizen, IT system consultation and change management.

Target Market(s)

Business to Business
Mainly to medium size - startup company

Industry/Entity Type

It Company

Coding

Coded - Design and coding required

Number of Pages Required

5+ page

Colors
0255a3
33a6d7
86cfc6
33b8a4
add136
cadf82
fbf289
fee18a
faa54b

Requirements
Must have
• We need Pages for
• Company mission
• Service Overview
• Contact
• Privacy Policy
• Terms and Conditions
• =========================
• As there were some questions, I add followings.---------
• 1. File Format
• We are going to use Amazon web services to upload finished web files.
• The finished files should be ready to use by simply replacing images and text.
• Please provide me "easy to handle" template with "sophisticated design".
• Thanks!
• 2. Multiple Languages
• We need buttons for changing language.
• We will have this translated to German, English and Japanese.
• Thank you so much!!
Nice to have
• These are current Logos and will be a next project to revise them...
• Attached Company Profile and Logo design
• 1. Company Profile
• 2. Our Company Logo
• 3. Our Product Logo -> This is most close to our image of design base.
• 4. Product Logo for PPT Header
• All just for your reference.
• ---------
• As there were some request, I added attachment as for contents for Our mission page.
Should not have
• I hope to see some unique designs.
• (Sorry please ignore my last update as I checked with our CEO.
• Bootstrap is absolutely good template.)

```html
<!DOCTYPE html>
<html lang="en">
<head>
<meta charset="utf-8">
<title>Orvane – Workflow tool veltor</title>
<link href="https://fonts.googleapis.com/css2?family=Barlow:wght@400;500;600;700&display=swap" rel="stylesheet">
<style>
:root{
  --green:#a4cb3d;
  --green-dark:#8db32b;
  --orange:#faa54b;
  --navy:#1d2433;
  --text:#2b2f36;
  --muted:#8a8f96;
  --pale-blue:#eaf5f8;
  --pale-yellow:#fdfbe6;
  --mint:#e3f3ee;
  --light:#f1f2f4;
  --white:#ffffff;
}
*{box-sizing:border-box;margin:0;padding:0}
html,body{width:1200px;height:3947px;overflow:hidden}
body{position:relative;background:var(--white);font-family:"Barlow",Arial,sans-serif;color:var(--text)}
.abs{position:absolute}
.center{text-align:center}
.section-title{position:absolute;left:0;width:1200px;text-align:center;color:var(--green);font-size:28px;font-weight:600}
.title-bar{position:absolute;left:583px;width:34px;height:3px;background:var(--orange)}
.btn{position:absolute;background:var(--green);color:var(--white);font-size:13px;font-weight:600;border-radius:20px;text-align:center;line-height:26px;height:26px}

/* header */
.topbar-item{position:absolute;top:16px;display:flex;align-items:center;gap:10px;font-size:12px;color:var(--text)}
.topbar-icon{width:22px;height:22px;border-radius:50%;background:#9fd3d0;display:flex;align-items:center;justify-content:center}
.nav{position:absolute;top:70px;font-size:13px;font-weight:600;color:var(--green-dark);display:flex;gap:30px}
.lang{position:absolute;top:14px;left:912px;display:flex;align-items:center;gap:8px;font-size:11px;color:var(--muted)}
.lang-dot{width:22px;height:22px;border-radius:50%;background:#c9323f}
.logo{position:absolute;display:flex;flex-direction:column;align-items:center;gap:4px}
.logo-circle{width:20px;height:20px;border-radius:50%;background:var(--green)}
.logo-name{font-size:18px;font-weight:600;color:var(--green-dark)}

/* hero */
.hero-title{position:absolute;left:288px;top:290px;font-size:46px;font-weight:600;color:var(--green)}
.hero-sub{position:absolute;left:310px;top:352px;font-size:17px;color:var(--muted)}
.hero-arrow{position:absolute;top:352px}
.illustration{position:absolute;left:660px;top:110px;width:420px;height:495px;border-radius:16px;background:linear-gradient(160deg,#dbeef3,#eef6f2 60%,#e9f2d3)}

/* welcome */
.welcome-lead{position:absolute;top:732px;left:0;width:1200px;text-align:center;font-size:14px;font-weight:600}
.welcome-text{position:absolute;top:758px;left:205px;width:790px;text-align:center;font-size:11px;line-height:15px;color:var(--muted)}
.pillar{position:absolute;top:868px;width:320px;text-align:center}
.pillar-icon{width:44px;height:44px;margin:0 auto}
.pillar h3{font-size:14px;font-weight:600;margin-top:10px}
.pillar p{font-size:11px;color:var(--muted);line-height:15px;margin-top:10px}

/* what we do */
.wwd-sub{position:absolute;top:1198px;left:0;width:1200px;text-align:center;font-size:13px;font-weight:600}
.hub-ring{position:absolute;left:455px;top:1237px;width:290px;height:290px;border-radius:50%;border:2px solid #eef0f2;background:var(--white)}
.hub{position:absolute;left:495px;top:1277px;width:210px;height:210px;border-radius:50%;background:var(--white);box-shadow:0 4px 22px rgba(0,0,0,.12);display:flex;align-items:center;justify-content:center}
.hub span{font-size:30px;font-weight:600;color:var(--green-dark)}
.feature-icon{position:absolute;width:42px;height:42px;border-radius:50%;background:var(--white);box-shadow:0 2px 10px rgba(0,0,0,.12);display:flex;align-items:center;justify-content:center}
.feature{position:absolute;font-size:11px;line-height:14px;color:var(--muted)}
.feature b{display:block;color:var(--text);font-weight:600;font-size:12px}

/* services */
.service-card{position:absolute;top:1803px;height:232px;background:var(--white);border-radius:14px;box-shadow:0 6px 18px rgba(0,0,0,.14);text-align:center;overflow:visible}
.service-top{height:72px;background:var(--mint);border-radius:14px 14px 0 0}
.service-icon{position:absolute;left:50%;top:22px;margin-left:-42px;width:84px;height:84px;border-radius:50%;background:var(--white);border:5px solid var(--mint);display:flex;align-items:center;justify-content:center}
.service-card h3{position:absolute;top:130px;left:0;width:100%;font-size:14px;font-weight:700}
.service-card p{position:absolute;top:158px;left:18px;right:18px;font-size:10px;line-height:13px;color:var(--muted)}
.plus{position:absolute;left:50%;bottom:-14px;margin-left:-14px;width:28px;height:28px;border-radius:50%;background:var(--orange);color:var(--white);font-weight:700;font-size:20px;line-height:27px}

/* gallery */
.photo{position:absolute;border:5px solid var(--white);box-shadow:0 3px 10px rgba(0,0,0,.15)}
.photo-caption{position:absolute;left:15px;right:15px;bottom:30px;height:66px;background:#1e88c2;color:var(--white);padding:12px 18px}
.photo-caption b{font-size:15px;font-weight:600;display:block}
.photo-caption span{font-size:10px;opacity:.85}

/* contact */
.field{position:absolute;background:var(--white);box-shadow:0 1px 5px rgba(0,0,0,.12);font-size:10px;color:var(--muted);padding:8px 12px}

/* clients */
.testimonial{position:absolute;top:3106px;width:380px}
.avatar{position:absolute;left:0;top:0;width:94px;height:94px;border-radius:50%;border:4px solid var(--white);box-shadow:0 2px 10px rgba(0,0,0,.15)}
.testimonial p{position:absolute;left:118px;top:6px;width:270px;font-size:11px;line-height:14px;color:var(--muted)}
.testimonial .name{position:absolute;left:118px;top:64px;font-size:11px;font-weight:600;color:var(--green-dark)}
.testimonial .stars{position:absolute;left:118px;top:80px;font-size:9px;color:var(--orange);letter-spacing:1px}
.quote{position:absolute;left:328px;top:60px;font-size:58px;color:#dde0e3;font-weight:700;line-height:1}
.partner{position:absolute;top:3302px;width:148px;height:58px;background:var(--white);box-shadow:0 2px 10px rgba(0,0,0,.08);display:flex;align-items:center;justify-content:center;font-size:18px;font-weight:600;color:#555a61}

/* footer */
.footer{position:absolute;left:0;top:3440px;width:1200px;height:468px;background:var(--navy);color:#d8dbe0}
.footer h4{position:absolute;top:130px;font-size:14px;font-weight:600;color:var(--white);letter-spacing:.5px}
.footer ul{position:absolute;top:172px;list-style:none;font-size:11px;line-height:31.6px}
.footer ul li::before{content:"› ";color:var(--green)}
.contact-line{position:absolute;display:flex;gap:12px;font-size:11px;line-height:15px}
.social{position:absolute;top:392px;left:412px;display:flex;gap:10px}
.social span{width:24px;height:24px;border-radius:50%;background:var(--green)}
.map{position:absolute;left:605px;top:172px;width:382px;height:170px;background:linear-gradient(135deg,#e9ece6,#dfe4dd 50%,#e8ebe5)}
.bottombar{position:absolute;left:0;top:3908px;width:1200px;height:39px;background:var(--green);color:var(--white);font-size:10px}
</style>
</head>
<body>

<svg class="abs" style="left:0;top:0" width="1200" height="3947" aria-hidden="true">
  <path d="M0 180 C120 150 230 240 260 370 C285 480 220 600 120 640 C60 660 20 650 0 640 Z" fill="var(--pale-blue)"/>
  <path d="M215 230 C280 180 360 215 360 300 L360 430 C360 500 300 540 240 520 Z" fill="#f3f9fb"/>
  <path d="M1200 720 C1110 760 1070 880 1120 980 C1150 1030 1180 1040 1200 1040 Z" fill="var(--pale-yellow)"/>
  <path d="M0 1040 C60 1080 80 1200 40 1320 L0 1360 Z" fill="var(--pale-yellow)"/>
  <path d="M1200 2080 C1120 2140 1080 2260 1120 2360 C1150 2420 1180 2430 1200 2430 Z" fill="var(--pale-blue)"/>
  <path d="M0 2990 C70 3030 140 3110 150 3220 C155 3300 80 3350 0 3350 Z" fill="#f4f9fb"/>
</svg>

<header>
  <div class="topbar-item" style="left:205px">
    <span class="topbar-icon"><svg width="12" height="12" viewBox="0 0 24 24"><path d="M6.6 10.8a15 15 0 0 0 6.6 6.6l2.2-2.2c.3-.3.7-.4 1-.2 1.1.4 2.3.6 3.6.6.6 0 1 .4 1 1V20c0 .6-.4 1-1 1A17 17 0 0 1 3 4c0-.6.4-1 1-1h3.5c.6 0 1 .4 1 1 0 1.3.2 2.5.6 3.6.1.3 0 .7-.2 1z" fill="#fff"/></svg></span>
    +100-555-0142
  </div>
  <div class="topbar-item" style="left:392px">
    <span class="topbar-icon"><svg width="12" height="12" viewBox="0 0 24 24"><rect x="2" y="5" width="20" height="14" rx="2" fill="#fff"/><path d="M3 6l9 7 9-7" stroke="#9fd3d0" stroke-width="2" fill="none"/></svg></span>
    info@orvane.com
  </div>
  <div class="lang"><span class="lang-dot"></span>Eng ⌄</div>
  <nav class="nav" style="left:205px"><span>Home</span><span>About Us</span><span>Our Product</span></nav>
  <nav class="nav" style="left:727px"><span>Our Service</span><span>Blogs</span><span>Contact Us</span></nav>
  <div class="logo" style="left:560px;top:40px;width:80px"><span class="logo-circle"></span><span class="logo-name">Orvane</span></div>
</header>

<section class="hero">
  <svg class="hero-arrow" style="left:45px" width="16" height="28" viewBox="0 0 16 28"><path d="M14 2L3 14l11 12" stroke="var(--green)" stroke-width="2.5" fill="none"/></svg>
  <svg class="hero-arrow" style="left:1133px" width="16" height="28" viewBox="0 0 16 28"><path d="M2 2l11 12L2 26" stroke="var(--green)" stroke-width="2.5" fill="none"/></svg>
  <h1 class="hero-title">The Main</h1>
  <p class="hero-sub">Is Our Product tool called "veltor".</p>
  <div class="btn" style="left:315px;top:400px;width:150px">Find Solution</div>
  <div class="illustration" role="img" aria-label="Illustration of two people working at laptops at a shared desk with floating app screens and icons above them"></div>
</section>

<section class="welcome">
  <div class="title-bar" style="top:678px"></div>
  <h2 class="section-title" style="top:684px">Welcome To Orvane</h2>
  <p class="welcome-lead">We need a web design for our product and for our company. And the main is our Product tool called "veltor".</p>
  <p class="welcome-text">Orvane helps teams plan, assign and follow work in one calm place. Our product tool veltor keeps every task visible, every owner clear and every deadline on time, so your people can focus on results and real progress instead of chasing updates across mail.</p>
  <div class="pillar" style="left:208px">
    <svg class="pillar-icon" viewBox="0 0 44 44"><circle cx="22" cy="22" r="18" fill="none" stroke="var(--green)" stroke-width="3"/><circle cx="22" cy="22" r="10" fill="none" stroke="var(--green)" stroke-width="3"/><circle cx="22" cy="22" r="3" fill="var(--green)"/><path d="M22 22L38 6" stroke="var(--orange)" stroke-width="3"/></svg>
    <h3>Our company's Goal</h3>
    <p>Make organization's communication smooth and healthy with<br>transparency and efficiency.</p>
  </div>
  <div class="pillar" style="left:661px">
    <svg class="pillar-icon" viewBox="0 0 44 44"><path d="M3 38L17 18l8 10 6-7 10 17Z" fill="none" stroke="var(--green)" stroke-width="3" stroke-linejoin="round"/><path d="M28 20V4h10l-3 4 3 4h-10" fill="none" stroke="var(--orange)" stroke-width="2.5"/></svg>
    <h3>Our Mission</h3>
    <p>Our mission is to achieve business goals with customers. We<br>work together to identify.</p>
  </div>
  <div class="btn" style="left:539px;top:1021px;width:122px">Read More</div>
</section>

<section class="what-we-do">
  <div class="title-bar" style="top:1144px"></div>
  <h2 class="section-title" style="top:1150px">What We Do</h2>
  <p class="wwd-sub">We have a workflow tool "veltor"</p>
  <div class="hub-ring"></div>
  <div class="hub"><span>veltor</span></div>

  <div class="feature" style="left:210px;top:1292px;width:205px"><b>Very simple end-user configurable</b>workflow for any company processes</div>
  <div class="feature-icon" style="left:424px;top:1295px"><svg width="16" height="16" viewBox="0 0 16 16"><circle cx="8" cy="5" r="3" fill="var(--green)"/><path d="M2 15c0-4 3-6 6-6s6 2 6 6z" fill="var(--green)"/></svg></div>

  <div class="feature" style="left:250px;top:1470px;width:170px;text-align:right"><b>Graphical &amp; amp</b>for features for startup users</div>
  <div class="feature-icon" style="left:434px;top:1463px"><svg width="16" height="16" viewBox="0 0 16 16"><circle cx="8" cy="8" r="6" fill="none" stroke="var(--green)" stroke-width="2"/><circle cx="8" cy="8" r="2.5" fill="var(--green)"/></svg></div>

  <div class="feature-icon" style="left:734px;top:1285px"><svg width="16" height="16" viewBox="0 0 16 16"><path d="M8 1c3 3 4 6 0 14C4 7 5 4 8 1z" fill="var(--green)"/></svg></div>
  <div class="feature" style="left:795px;top:1290px;width:200px"><b>Additional features</b>Multiple delegation Clear status for each owner. Task owner management console with due date reminders&amp;reporting</div>

  <div class="feature-icon" style="left:724px;top:1463px"><svg width="16" height="16" viewBox="0 0 16 16"><path d="M8 1a4 4 0 0 0-4 4v4l-2 3h12l-2-3V5a4 4 0 0 0-4-4zM6 13a2 2 0 0 0 4 0z" fill="var(--green)"/></svg></div>
  <div class="feature" style="left:795px;top:1470px;width:210px"><b>Simple and easy task control with</b>outlook e-mail look &amp; feel</div>

  <div class="feature-icon" style="left:579px;top:1524px"><svg width="16" height="16" viewBox="0 0 16 16"><path d="M3 13l4-4M7 9l2 2 5-5-2-2-5 5zM2 14l2-1-1-1z" stroke="var(--green)" stroke-width="2" fill="none"/></svg></div>
  <div class="feature center" style="left:450px;top:1582px;width:300px"><b>Non charged skill up guidance</b></div>
</section>

<section class="services">
  <svg class="abs" style="left:0;top:1600px" width="1200" height="390" aria-hidden="true">
    <path d="M0 30 C250 90 450 80 650 60 C850 40 1050 0 1200 20 L1200 390 L0 390 Z" fill="var(--green)"/>
  </svg>
  <div class="title-bar" style="top:1730px;background:var(--orange)"></div>
  <h2 class="section-title" style="top:1738px;color:var(--white)">Our Service</h2>

  <div class="service-card" style="left:207px;width:244px">
    <div class="service-top"></div>
    <div class="service-icon"><svg width="44" height="44" viewBox="0 0 44 44"><circle cx="22" cy="22" r="21" fill="var(--orange)"/><path d="M22 9a9 9 0 0 0-5 16v4h10v-4a9 9 0 0 0-5-16zM18 32h8v3h-8z" fill="#fff"/></svg></div>
    <h3>Implementation Service</h3>
    <p>Our client list includes a wide variety of small to medium to major sized enterprises.</p>
    <div class="plus">+</div>
  </div>
  <div class="service-card" style="left:483px;width:229px">
    <div class="service-top"></div>
    <div class="service-icon"><svg width="44" height="44" viewBox="0 0 44 44"><circle cx="22" cy="22" r="21" fill="var(--orange)"/><circle cx="18" cy="16" r="5" fill="#fff"/><path d="M8 33c0-6 4-9 10-9s10 3 10 9z" fill="#fff"/><circle cx="30" cy="26" r="6" fill="none" stroke="#fff" stroke-width="3"/></svg></div>
    <h3>Project Management Service</h3>
    <p>We will provide end-to-end PM service with experienced PM.</p>
    <div class="plus">+</div>
  </div>
  <div class="service-card" style="left:753px;width:227px">
    <div class="service-top"></div>
    <div class="service-icon"><svg width="44" height="44" viewBox="0 0 44 44"><circle cx="22" cy="22" r="21" fill="var(--orange)"/><circle cx="22" cy="17" r="6" fill="#fff"/><path d="M11 34c0-7 5-10 11-10s11 3 11 10z" fill="#fff"/><path d="M14 18a8 8 0 0 1 16 0" stroke="#fff" stroke-width="2" fill="none"/></svg></div>
    <h3>Consultation Service</h3>
    <p>Consulting services to a wide range of fields such as creating business strategy.</p>
    <div class="plus">+</div>
  </div>
</section>

<section class="gallery">
  <div class="title-bar" style="top:2126px"></div>
  <h2 class="section-title" style="top:2134px">See Our Gallery</h2>
  <div class="photo" style="left:208px;top:2224px;width:242px;height:126px;background:linear-gradient(135deg,#7aa8c8,#c9d5df)" role="img" aria-label="Photo of a smiling team gathered around a cloud symbol"></div>
  <div class="photo" style="left:208px;top:2382px;width:242px;height:126px;background:linear-gradient(135deg,#0f2a4a,#2c6b9a)" role="img" aria-label="Photo of a glowing digital network over a dark blue background"></div>
  <div class="photo" style="left:471px;top:2224px;width:247px;height:284px;background:linear-gradient(160deg,#3d4a5a,#8a9bab)" role="img" aria-label="Photo of colleagues in business clothes talking in an office">
    <div class="photo-caption"><b>Lorem ipsum dolor</b><span>Team planning session, spring</span></div>
  </div>
  <div class="photo" style="left:745px;top:2224px;width:237px;height:126px;background:linear-gradient(135deg,#5a5f66,#c0c4c8)" role="img" aria-label="Photo of people working together on a laptop"></div>
  <div class="photo" style="left:745px;top:2382px;width:237px;height:126px;background:linear-gradient(135deg,#8c7a66,#d8cfc4)" role="img" aria-label="Photo of a small group meeting around a table with a laptop"></div>
</section>

<section class="contact">
  <div class="abs" style="left:0;top:2566px;width:1200px;height:395px;background:linear-gradient(90deg,#f3f4f6,#e6e8eb)"></div>
  <div class="abs" style="left:79px;top:2540px;width:368px;height:421px;background:linear-gradient(180deg,#c9b39a,#2c2f36 55%,#3b3f47)" role="img" aria-label="Photo of a businesswoman holding a laptop showing the website"></div>
  <div class="title-bar" style="left:676px;top:2624px"></div>
  <h2 class="section-title" style="left:492px;width:495px;top:2632px">Contact Us</h2>
  <div class="field" style="left:492px;top:2690px;width:243px;height:37px">Name</div>
  <div class="field" style="left:745px;top:2690px;width:242px;height:37px">Email</div>
  <div class="field" style="left:492px;top:2737px;width:243px;height:40px">Phone</div>
  <div class="field" style="left:745px;top:2737px;width:242px;height:40px">Service</div>
  <div class="field" style="left:492px;top:2790px;width:495px;height:71px">Message</div>
  <div class="btn" style="left:677px;top:2893px;width:120px">Send Now</div>
</section>

<section class="clients">
  <div class="title-bar" style="top:3024px"></div>
  <h2 class="section-title" style="top:3032px">Meet Our New Clients</h2>
  <svg class="abs" style="left:120px;top:3128px" width="12" height="22" viewBox="0 0 12 22"><path d="M10 2L2 11l8 9" stroke="#c8ccd0" stroke-width="2" fill="none"/></svg>
  <svg class="abs" style="left:1062px;top:3128px" width="12" height="22" viewBox="0 0 12 22"><path d="M2 2l8 9-8 9" stroke="#c8ccd0" stroke-width="2" fill="none"/></svg>

  <div class="testimonial" style="left:208px">
    <div class="avatar" style="background:linear-gradient(135deg,#d6b79c,#8e7260)" role="img" aria-label="Portrait photo of client Martin Ellis Crane"></div>
    <p>Lorem ipsum dolor sit amet, consectetur adipiscing elit. Etiam ullamcorper turpis scelerisque, aliquet orci in, sollicitudin augue.</p>
    <span class="name">Martin Ellis Crane</span>
    <span class="stars">★★★★★</span>
    <span class="quote">”</span>
  </div>
  <div class="testimonial" style="left:624px">
    <div class="avatar" style="background:linear-gradient(135deg,#e6c9a8,#a07e5c)" role="img" aria-label="Portrait photo of client Lena Varga"></div>
    <p>Lorem ipsum dolor sit amet, consectetur adipiscing elit. Etiam ullamcorper turpis scelerisque, aliquet orci in, sollicitudin augue.</p>
    <span class="name">Lena Varga</span>
    <span class="stars">★★★★★</span>
    <span class="quote">”</span>
  </div>

  <div class="partner" style="left:208px">Tidewell</div>
  <div class="partner" style="left:367px">Norrow</div>
  <div class="partner" style="left:526px">Upwardly</div>
  <div class="partner" style="left:685px">Stonefield</div>
  <div class="partner" style="left:844px">Brightloom</div>
</section>

<footer>
  <svg class="abs" style="left:0;top:3390px" width="1200" height="100" aria-hidden="true">
    <path d="M0 70 C300 60 600 10 1200 20 L1200 100 L0 100 Z" fill="var(--navy)"/>
    <path d="M0 58 C300 50 650 0 1200 8 L1200 20 C600 10 300 62 0 70 Z" fill="var(--green)"/>
  </svg>
  <div class="footer">
    <div class="logo" style="left:560px;top:30px;width:80px"><span class="logo-circle"></span><span class="logo-name" style="color:var(--green)">Orvane</span></div>
    <h4 style="left:205px">QUICK LINKS</h4>
    <ul style="left:205px">
      <li>Home</li><li>About Us</li><li>Service</li><li>Clients Testimonials</li><li>Our Blogs</li><li>Contact Us</li>
    </ul>
    <h4 style="left:395px">CONTACT INFO</h4>
    <div class="contact-line" style="left:397px;top:176px">
      <svg width="12" height="14" viewBox="0 0 12 14"><path d="M6 0a5 5 0 0 0-5 5c0 4 5 9 5 9s5-5 5-9a5 5 0 0 0-5-5zm0 7a2 2 0 1 1 0-4 2 2 0 0 1 0 4z" fill="var(--green)"/></svg>
      <span>B - 2071 Marlow<br>Quayside Rd. 8</span>
    </div>
    <div class="contact-line" style="left:397px;top:242px">
      <svg width="12" height="12" viewBox="0 0 24 24"><path d="M6.6 10.8a15 15 0 0 0 6.6 6.6l2.2-2.2c.3-.3.7-.4 1-.2 1.1.4 2.3.6 3.6.6.6 0 1 .4 1 1V20c0 .6-.4 1-1 1A17 17 0 0 1 3 4c0-.6.4-1 1-1h3.5c.6 0 1 .4 1 1 0 1.3.2 2.5.6 3.6.1.3 0 .7-.2 1z" fill="var(--green)"/></svg>
      <span>610-555-0188</span>
    </div>
    <div class="contact-line" style="left:397px;top:282px">
      <svg width="12" height="12" viewBox="0 0 24 24"><rect x="2" y="5" width="20" height="14" rx="2" fill="var(--green)"/><path d="M3 6l9 7 9-7" stroke="var(--navy)" stroke-width="2" fill="none"/></svg>
      <span>info@orvane.com</span>
    </div>
    <div class="social"><span></span><span></span><span></span></div>
    <h4 style="left:605px">LOCATION MAP</h4>
    <div class="map" role="img" aria-label="Street map showing the office location"></div>
  </div>
  <div class="bottombar">
    <span class="abs" style="left:205px;top:13px">©Copyright 2018, Orvane All Rights Reserved.</span>
    <span class="abs" style="left:900px;top:13px">Privacy &nbsp;·&nbsp; Policy</span>
  </div>
</footer>

</body>
</html>
```